Flyer Template

I need a flyer template for door knocking on properties. Text Boxes need to be editable, with a header and text body. Footer to be my info. Project to be stylized to match my real estate signs and logo art from past projects

```html
<!DOCTYPE html>
<html lang="en">
<head>
<meta charset="utf-8">
<title>Marlowe Realty – Door Knocking Flyer</title>
<link rel="stylesheet" href="https://fonts.googleapis.com/css2?family=Montserrat:ital,wght@0,500;0,600;0,700;0,800;1,600&display=swap">
<style>
  :root {
    --page-bg: #b7b8ba;
    --ink: #111111;
    --white: #ffffff;
    --red: #e31e26;
    --red-deep: #8c1418;
    --ring-grey: #5b5c5f;
    --sky: #9ec3e4;
    --foliage: #5f8c4a;
    --wall: #c9a07a;
  }
  html, body {
    margin: 0;
    width: 1200px;
    height: 1200px;
    overflow: hidden;
    background: var(--page-bg);
    font-family: "Montserrat", sans-serif;
  }
  .flyer-frame {
    position: absolute;
    left: 187px;
    top: 65px;
    width: 826px;
    height: 1070px;
    overflow: hidden;
  }
  .flyer {
    position: absolute;
    left: 0;
    top: 0;
    width: 1033px;
    height: 1337px;
    transform: scale(0.8);
    transform-origin: 0 0;
    background: var(--white);
    overflow: hidden;
  }
  .flyer-art {
    position: absolute;
    inset: 0;
    width: 1033px;
    height: 1337px;
  }
  .brand-box {
    position: absolute;
    left: 746px;
    top: 0;
    width: 241px;
    height: 231px;
    background: var(--white);
    display: flex;
    align-items: flex-end;
    justify-content: center;
    padding-bottom: 26px;
    box-sizing: border-box;
  }
  .brand-name {
    margin: 0;
    font-weight: 700;
    font-size: 27px;
    line-height: 37px;
    text-align: center;
    color: var(--ink);
    letter-spacing: 0.5px;
  }
  .headline {
    position: absolute;
    left: 63px;
    top: 576px;
    margin: 0;
    color: var(--ink);
    font-weight: 700;
  }
  .headline span { display: block; }
  .headline .line-small { font-size: 58px; line-height: 66px; letter-spacing: 1px; }
  .headline .line-title { font-size: 64px; line-height: 68px; color: var(--red); font-weight: 800; }
  .headline .line-slogan { font-size: 53px; line-height: 68px; letter-spacing: 1px; }
  .rule {
    position: absolute;
    height: 11px;
    background: var(--ink);
  }
  .rule--left { left: 70px; top: 797px; width: 167px; }
  .rule--right { left: 828px; top: 1163px; width: 167px; }
  .body-copy {
    position: absolute;
    margin: 0;
    font-weight: 600;
    font-size: 23.5px;
    line-height: 30.4px;
    letter-spacing: 1px;
  }
  .body-copy--left { left: 70px; top: 834px; width: 480px; color: var(--ink); }
  .body-copy--right { right: 38px; top: 827px; width: 330px; color: var(--white); text-align: right; }
  .price-block {
    position: absolute;
    right: 40px;
    top: 625px;
    text-align: right;
    color: var(--white);
  }
  .price-label { display: block; font-weight: 700; font-size: 33px; letter-spacing: 3px; line-height: 44px; }
  .price-value { display: block; font-weight: 800; font-size: 66px; line-height: 72px; }
  .contact {
    position: absolute;
    right: 40px;
    top: 1180px;
    text-align: right;
    color: var(--white);
  }
  .contact-label { display: block; font-weight: 700; font-size: 24px; line-height: 30px; }
  .contact-phone { display: block; font-weight: 800; font-size: 35px; line-height: 46px; letter-spacing: 2px; margin-top: 4px; }
  .contact-email { display: block; font-weight: 600; font-style: italic; font-size: 36px; line-height: 50px; letter-spacing: 1.5px; }
</style>
</head>
<body>
  <div class="flyer-frame">
    <main class="flyer">
      <svg class="flyer-art" viewBox="0 0 1033 1337" aria-hidden="false">
        <defs>
          <linearGradient id="photoTone" x1="0" y1="0" x2="0" y2="1">
            <stop offset="0" stop-color="var(--sky)"/>
            <stop offset="0.45" stop-color="var(--wall)"/>
            <stop offset="1" stop-color="var(--foliage)"/>
          </linearGradient>
          <linearGradient id="redPanel" x1="0" y1="0" x2="1" y2="0">
            <stop offset="0.35" stop-color="var(--red-deep)"/>
            <stop offset="1" stop-color="var(--red)"/>
          </linearGradient>
        </defs>
        <rect class="property-photo" x="0" y="0" width="1033" height="572" fill="url(#photoTone)" role="img" aria-label="Photo of a modern two-storey house with wooden gate, garden and trees"/>
        <g class="photo-accents" stroke="var(--white)" stroke-width="5" stroke-linecap="square">
          <line x1="0" y1="362" x2="115" y2="247"/>
          <line x1="0" y1="425" x2="250" y2="172"/>
          <line x1="797" y1="313" x2="880" y2="232"/>
          <line x1="930" y1="240" x2="1033" y2="75"/>
        </g>
        <rect class="price-band" x="400" y="572" width="633" height="228" fill="var(--ink)"/>
        <rect class="info-panel" x="0" y="799" width="1033" height="538" fill="url(#redPanel)"/>
        <circle class="ring" cx="175" cy="902" r="470" fill="var(--ring-grey)"/>
        <circle class="title-disc" cx="180" cy="902" r="430" fill="var(--white)"/>
        <g class="contact-icon">
          <circle cx="669" cy="1226" r="30" fill="var(--white)"/>
          <rect x="658" y="1216" width="26" height="19" rx="2" fill="none" stroke="var(--red)" stroke-width="3"/>
          <polyline points="658,1217 671,1228 684,1217" fill="none" stroke="var(--red)" stroke-width="3"/>
          <path d="M652 1205 h8 v30 h-8 z" fill="var(--red)"/>
        </g>
      </svg>

      <div class="brand-box">
        <p class="brand-name">MARLOWE<br>REALTY</p>
      </div>

      <h1 class="headline">
        <span class="line-small">YOUR</span>
        <span class="line-title">TITLE HERE</span>
        <span class="line-slogan">YOUR SALOGAN</span>
      </h1>
      <div class="rule rule--left"></div>
      <p class="body-copy body-copy--left">Lorem ipsum dolor sit amet, consectetuer adipiscing elit, sed diam nonummy nibh euismod tincidunt ut laoreet dolore magna aliquam erat volutpat. Ut wisi enim ad minim veniam, quis nostrud exerci tation ullamcorper suscipit lobortis, Lorem ipsum dolor sit amet, consectetuer adipiscing elit, Lorem ipsum dolor sit amet, consectetuer adipiscing elit,</p>

      <div class="price-block">
        <span class="price-label">TEXT HER</span>
        <span class="price-value">$000,00</span>
      </div>

      <p class="body-copy body-copy--right">Lorem ipsum dolor sit amet, consectetuer adipiscing elit, sed diam nonummy nibh euismod tincidunt ut laoreet dolore magna aliquam erat volutpat. Ut wisi enim ad minim veniam, quis nostrud exerci tation</p>

      <div class="rule rule--right"></div>
      <div class="contact">
        <span class="contact-label">Call Now :</span>
        <span class="contact-phone">555-214-0187</span>
        <span class="contact-email">dmarlowe@mailbox.com</span>
      </div>
    </main>
  </div>
</body>
</html>
```